Business Advisory Firm Business Card

A clean, very upscale looking business card. Not crowded.

Please include logo (attached) and:

Danielle R. Kastrup
Four Ashgrove Court
New York, NY 10087
tel: (917) 555-3140
fax: (646) 555-2973
email: dkastrup@silvermerepartners.example
website: www.silvermerepartners.example

Target Market(s)

Business clients. Often real estate development firms, other advisory firms or growing companies that need assistance. I would like a card that looks impressive and confident.

Industry/Entity Type

Business

Colors

Designer to choose colors to be used in the design.

Requirements
Must have
• Impressive and confident. Please include logo.
Should not have
• nothing flashy...

```html
<!DOCTYPE html>
<html lang="en">
<head>
<meta charset="utf-8">
<title>Silvermere Advisory Partners – Business Card</title>
<link rel="stylesheet" href="https://fonts.googleapis.com/css2?family=Questrial&family=Libre+Baskerville:wght@700&family=Arimo&display=swap">
<style>
  :root {
    --canvas: #ffffff;
    --card: #ffffff;
    --card-edge: #2a2a2a;
    --leaf-green: #a9cf46;
    --pale-block: #ececec;
    --ink: #333333;
    --ink-soft: #3a3a3a;
  }
  * { margin: 0; padding: 0; box-sizing: border-box; }
  html, body {
    width: 1200px;
    height: 818px;
    overflow: hidden;
    background: var(--canvas);
  }
  .business-card {
    position: absolute;
    left: 110px;
    top: 129px;
    width: 980px;
    height: 560px;
    background: var(--card);
    border: 1px solid var(--card-edge);
    overflow: hidden;
  }
  .card-swoosh {
    position: absolute;
    inset: 0;
    width: 100%;
    height: 100%;
  }
  .brand-mark {
    position: absolute;
    left: 84px;
    top: 68px;
    width: 130px;
    height: 130px;
    background: var(--leaf-green);
  }
  .brand-name {
    position: absolute;
    left: 262px;
    top: 84px;
    font-family: "Questrial", sans-serif;
    font-variant: small-caps;
    font-size: 36px;
    line-height: 32px;
    letter-spacing: 0.5px;
    color: var(--ink-soft);
  }
  .corner-block {
    position: absolute;
    right: -40px;
    top: -30px;
    width: 290px;
    height: 330px;
    background: linear-gradient(160deg, #f1f1f1, var(--pale-block));
    opacity: 0.8;
  }
  .holder-name {
    position: absolute;
    left: 0;
    width: 100%;
    padding-left: 40px;
    top: 288px;
    text-align: center;
    font-family: "Libre Baskerville", serif;
    font-weight: 700;
    font-size: 31px;
    color: var(--ink);
  }
  .contact-lines {
    position: absolute;
    left: 28px;
    top: 422px;
    font-family: "Arimo", sans-serif;
    font-size: 22px;
    line-height: 33px;
    color: var(--ink);
    list-style: none;
  }
</style>
</head>
<body>
  <article class="business-card">
    <svg class="card-swoosh" viewBox="0 0 980 560" preserveAspectRatio="none" aria-hidden="true">
      <path d="M0,177 C150,385 300,450 480,447 C700,444 870,422 980,378 L980,560 L0,560 Z" fill="var(--leaf-green)"/>
    </svg>
    <div class="corner-block" aria-hidden="true"></div>

    <div class="brand-mark" aria-hidden="true"></div>
    <h1 class="brand-name">Silvermere<br>Advisory<br>Partners, Inc.</h1>

    <p class="holder-name">Danielle R. Kastrup</p>

    <ul class="contact-lines">
      <li>Four Ashgrove Court - New York, NY 10087</li>
      <li>tel: (917) 555-3140 - fax: (646) 555-2973</li>
      <li>e.mail: dkastrup@silvermerepartners.example - &nbsp;www.silvermerepartners.example</li>
    </ul>
  </article>
</body>
</html>
```